A modern web page for a software product

We need a web page for a software product, which is an advanced solution based on Machine Learning and Natural Language processing. We already have a logo of the product and expect the web page to be inline with the logo colors. The design should be for one page web site with scrolled sections - details of the content and guidelines in the attachments.

Target Market(s)

software company

Industry/Entity Type

It Company

Number of Pages Required

1 page

Colors

Designer to choose colors to be used in the design.

Requirements
Must have
• - modern icons and graphics
• - inline with the logo colors
• - be related to Machine Learining, AI, data processing
• - should have two language versions: english and polish both are attached.
Nice to have
• - animation/motion
Should not have
• - any photos embedded

```html
<!DOCTYPE html>
<html lang="en">
<head>
<meta charset="utf-8">
<title>Discovery &amp; Classification of Personal Data</title>
<link rel="stylesheet" href="https://fonts.googleapis.com/css2?family=Raleway:wght@300;400;600;700&family=Roboto:wght@300;400;500;700&display=swap">
<style>
  :root {
    --navy: #1f3a6d;
    --teal: #17b8b1;
    --cyan: #1fc4d6;
    --slate: #3d4a6b;
    --muted: #4d5c84;
    --gray: #6b7590;
    --mist: #e8f7f7;
    --white: #ffffff;
    --sun: #f6c063;
    --blue: #3f7fd6;
  }
  * { margin: 0; padding: 0; box-sizing: border-box; }
  html, body { width: 1200px; height: 1200px; overflow: hidden; background: var(--white); }
  .page { position: relative; width: 1200px; height: 1200px; font-family: "Roboto", sans-serif; }

  .brand { position: absolute; left: 150px; top: 34px; font-family: "Raleway", sans-serif; font-weight: 700; font-size: 28px; color: var(--navy); letter-spacing: 0.5px; }
  .nav { position: absolute; top: 41px; left: 0; }
  .nav a { position: absolute; white-space: nowrap; font-size: 12.5px; font-weight: 500; color: var(--slate); text-decoration: none; letter-spacing: 0.2px; }
  .nav a.active { padding-bottom: 6px; border-bottom: 2px solid var(--teal); }

  .cloud { position: absolute; background: var(--mist); border-radius: 30px; }

  .hero-title { position: absolute; left: 0; width: 1200px; top: 167px; text-align: center; font-family: "Raleway", sans-serif; font-weight: 700; font-size: 36px; line-height: 45px; color: var(--navy); }
  .hero-sub { position: absolute; left: 0; width: 1200px; top: 279px; text-align: center; font-family: "Raleway", sans-serif; font-weight: 300; font-size: 15.5px; line-height: 24px; color: var(--slate); }
  .btn { position: absolute; left: 525px; top: 361px; width: 150px; height: 41px; background: var(--teal); color: var(--white); font-size: 12px; font-weight: 700; display: flex; align-items: center; justify-content: center; box-shadow: 0 3px 6px rgba(23,184,177,0.3); }

  .art { position: absolute; }
  .art-left { left: 0; top: 256px; width: 320px; height: 238px; background: linear-gradient(135deg, #f6c063 0%, #3f7fd6 45%, #2b5aa8 100%); opacity: 0.85; }
  .art-right { left: 868px; top: 248px; width: 332px; height: 246px; background: linear-gradient(225deg, #f6c063 0%, #2fcf8f 30%, #3f7fd6 65%, #1f3a6d 100%); opacity: 0.85; }
  .art-f1 { left: 760px; top: 730px; width: 118px; height: 131px; background: linear-gradient(160deg, #9aa3b2 0%, #17b8b1 40%, #3f7fd6 100%); border-radius: 4px; }
  .art-f2 { left: 318px; top: 972px; width: 232px; height: 134px; background: linear-gradient(120deg, #3f7fd6 0%, #d9dde4 50%, #f6c063 100%); border-radius: 4px; }

  .section-title { position: absolute; left: 0; width: 1200px; top: 580px; text-align: center; font-family: "Raleway", sans-serif; font-weight: 600; font-size: 29px; color: var(--navy); }
  .title-ornament { position: absolute; left: 501px; top: 625px; width: 197px; height: 16px; border-radius: 8px; background: linear-gradient(90deg, rgba(31,196,214,0.35), rgba(31,196,214,0.6), rgba(31,196,214,0.35)); }

  .feature-num { position: absolute; font-family: "Roboto", sans-serif; font-weight: 400; font-size: 50px; line-height: 50px; color: var(--blue); }
  .feature-rule { position: absolute; width: 1px; background: #9fb2d6; }
  .feature-head { position: absolute; font-size: 16px; line-height: 24px; color: var(--muted); white-space: nowrap; }
  .feature-list { position: absolute; left: 316px; top: 779px; width: 420px; list-style: none; }
  .feature-list li { position: relative; padding-left: 14px; font-size: 12px; line-height: 16px; font-weight: 300; color: var(--gray); margin-bottom: 8px; white-space: nowrap; }
  .feature-list li::before { content: ""; position: absolute; left: 0; top: 5px; width: 5px; height: 5px; border-radius: 50%; background: var(--teal); }
</style>
</head>
<body>
<div class="page">
  <header>
    <div class="brand">LOGO</div>
    <nav class="nav">
      <a class="active" style="left:370px">MAIN FEATURES</a>
      <a style="left:522px">USE CASES</a>
      <a style="left:644px">HIGHLIGHTS</a>
      <a style="left:774px">CONTACT</a>
    </nav>
  </header>

  <section class="hero">
    <div class="cloud" style="left:-30px; top:100px; width:314px; height:48px; border-radius:0 24px 24px 0;"></div>
    <div class="cloud" style="left:124px; top:148px; width:180px; height:84px;"></div>
    <div class="cloud" style="left:-30px; top:188px; width:272px; height:44px; border-radius:0 22px 22px 0;"></div>
    <div class="cloud" style="left:50px; top:232px; width:250px; height:50px;"></div>
    <div class="cloud" style="left:978px; top:98px; width:240px; height:42px; border-radius:22px 0 0 22px;"></div>
    <div class="cloud" style="left:1068px; top:130px; width:150px; height:42px; border-radius:22px 0 0 22px;"></div>
    <div class="cloud" style="left:980px; top:150px; width:162px; height:58px;"></div>
    <div class="cloud" style="left:922px; top:208px; width:290px; height:58px; border-radius:30px 0 0 30px;"></div>

    <div class="art art-left" role="img" aria-label="Line illustration of servers, a camera, envelope, binary code and cloud upload"></div>
    <div class="art art-right" role="img" aria-label="Line illustration of a security shield, key, magnifier and server racks"></div>

    <h1 class="hero-title">Discovery &amp; Classification<br>of Personal Data</h1>
    <p class="hero-sub">Advanced software solution based on Machine Learning<br>and Natural Language processing</p>
    <div class="btn">LEARN MORE</div>
  </section>

  <section class="features">
    <h2 class="section-title">Main Features</h2>
    <div class="title-ornament" role="img" aria-label="Decorative zigzag line of small circles"></div>

    <div class="feature-num" style="left:264px; top:716px;">1</div>
    <div class="feature-rule" style="left:298px; top:724px; height:36px;"></div>
    <h3 class="feature-head" style="left:315px; top:718px; font-weight:400;">Detection of personal and sensitive data<br>for GDPR compliance</h3>
    <ul class="feature-list">
      <li>in structural sources (e.g. SQL servers)</li>
      <li>in unstructured sources (e.g.: documents, e-mails, logs, data streams)</li>
      <li>in "noisy" content written in natural language (e.g.: containing errors<br>or custom formats)</li>
      <li>built in ML models and rules for personal data used in Poland</li>
    </ul>
    <div class="art art-f1" role="img" aria-label="Illustration of a user profile on a browser window beside a phone"></div>

    <div class="art art-f2" role="img" aria-label="Illustration of a document under a magnifier with text tag, stopwatch and chart"></div>
    <div class="feature-num" style="left:646px; top:1010px;">2</div>
    <div class="feature-rule" style="left:690px; top:1016px; height:36px;"></div>
    <h3 class="feature-head" style="left:707px; top:1011px; font-weight:400;">Fast cataloging and classification<br>of data and sources</h3>
  </section>
</div>
</body>
</html>
```